Restaurant Business Card Template

I need a business card created in the same color scheme and style as the attached label. Preferably it'd be in a .ai format.

Industry/Entity Type

German Restaurant

Contact Information for Business Card

Verna Tollick, Front of House Manager, 312.774.2190, verna@brunfeldstuberestaurant.com, info@brunfeldstuberestaurant.com, 416 Birch Ave., Lower Level, Hollenbrook, OR 97342.

Requirements
Must have
• Matching fonts and colors.
Nice to have
• If not able to match secondary font, something similar.

```html
<!DOCTYPE html>
<html lang="en">
<head>
<meta charset="utf-8">
<title>Brunfeldstube Restaurant – Business Card</title>
<link rel="stylesheet" href="https://fonts.googleapis.com/css2?family=Oswald:wght@300;400;500&display=swap">
<style>
  :root {
    --page-bg: #e4e4e4;
    --parchment-top: #ecdcb8;
    --parchment-mid: #f4ead3;
    --paper-white: #fdfcf8;
    --ink: #222222;
    --gold: #a8893a;
    --gold-icon: #c2a55a;
    --bavarian-blue: #8fb0cc;
  }
  * { margin: 0; padding: 0; box-sizing: border-box; }
  html, body {
    width: 1200px; height: 1200px; overflow: hidden;
    background: var(--page-bg);
    font-family: "Oswald", sans-serif;
  }
  .card {
    position: absolute;
    left: 50px; top: 286px;
    width: 1100px; height: 628px;
    background: linear-gradient(180deg, var(--parchment-top) 0%, var(--parchment-mid) 45%, var(--paper-white) 100%);
    overflow: hidden;
  }
  .card__pattern {
    position: absolute; left: 0; top: 0;
    width: 100%; height: 200px;
    background: linear-gradient(180deg, rgba(143,176,204,0.45) 0%, rgba(143,176,204,0.18) 55%, rgba(143,176,204,0) 100%);
  }
  .brand {
    position: absolute;
    left: 0; right: 0; top: 130px;
    display: flex; align-items: center; justify-content: center; gap: 16px;
    color: var(--ink);
    font-weight: 500;
    font-size: 46px;
    letter-spacing: 1px;
  }
  .brand__mark {
    width: 26px; height: 26px; border-radius: 50%;
    background: var(--ink);
  }
  .contact {
    position: absolute; left: 69px; top: 418px;
    list-style: none;
    color: var(--ink);
    font-weight: 400;
    font-size: 25px;
    line-height: 31px;
  }
  .contact__item { display: flex; align-items: flex-start; }
  .contact__icon { width: 20px; height: 20px; margin: 6px 16px 0 0; flex: none; fill: var(--gold-icon); }
  .contact__icon--blank { visibility: hidden; }
  .person {
    position: absolute; right: 55px; top: 380px;
    text-align: right;
  }
  .person__name {
    color: var(--ink);
    font-weight: 500;
    font-size: 66px;
    line-height: 74px;
  }
  .person__title {
    color: var(--gold);
    font-weight: 400;
    font-size: 28px;
    line-height: 32px;
  }
</style>
</head>
<body>
  <article class="card">
    <div class="card__pattern" role="img" aria-label="Faded blue and white Bavarian diamond pattern across the top edge"></div>

    <div class="brand">
      <span class="brand__mark"></span>
      <span class="brand__name">Brunfeldstube Restaurant</span>
    </div>

    <ul class="contact">
      <li class="contact__item">
        <svg class="contact__icon" viewBox="0 0 20 20"><path d="M4 2l3 0 2 4-2 2c1 2 3 4 5 5l2-2 4 2v3c0 1-1 2-2 2C9 18 2 11 2 4c0-1 1-2 2-2z"/></svg>
        <span>+312 -774- 2190</span>
      </li>
      <li class="contact__item">
        <svg class="contact__icon" viewBox="0 0 20 20"><path d="M1 4h18v12H1z"/><path d="M2 5l8 6 8-6" fill="none" stroke="#fdfcf8" stroke-width="1.5"/></svg>
        <span>verna@brunfeldstuberestaurant.com</span>
      </li>
      <li class="contact__item">
        <svg class="contact__icon" viewBox="0 0 20 20"><path d="M1 4h18v12H1z"/><path d="M2 5l8 6 8-6" fill="none" stroke="#fdfcf8" stroke-width="1.5"/></svg>
        <span>info@brunfeldstuberestaurant.com</span>
      </li>
      <li class="contact__item">
        <svg class="contact__icon" viewBox="0 0 20 20"><path d="M10 1a6 6 0 0 1 6 6c0 5-6 12-6 12S4 12 4 7a6 6 0 0 1 6-6z"/><circle cx="10" cy="7" r="2.2" fill="#fdfcf8"/></svg>
        <span>416 Birch Ave. Lower Level</span>
      </li>
      <li class="contact__item">
        <svg class="contact__icon contact__icon--blank" viewBox="0 0 20 20"></svg>
        <span>Hollenbrook. OR 97342. Deadline</span>
      </li>
    </ul>

    <div class="person">
      <h1 class="person__name">Verna Tollick</h1>
      <p class="person__title">Front of House Manager</p>
    </div>
  </article>
</body>
</html>
```